i would like a business card to leave with customers and potential customers for electrical work and for the supply and install of reverse cycle airconditioning in the domestic and commercial market.
I own my own business and im a sole trader. I have an a'class electrical lisence and also a refrigeration lisence so i am
able to offer complete installations in airconditioning by a fully qualified and lisenced tradesman.
im looking for something that comes across as unique and professional.
i had the coluor black and some gold in mind but open to any coluors.
something like Beacon Electrical & Refrigeration
or Beacon Air.
i will use this design on a business card to advertise through summer to help generate installs through the busy season.

Target Market(s)

Mainly domestic house holds through summer who are in need of airconditioning and reliable information to acomadate thier cooling and heating requirements

Industry/Entity Type

Electrical

Requirements
Must have
• Business name- Beacon
My name- Peter Wollaston
My mobile no- 0457 819 302
My email- prwollaston@tarvel.com.au
Installation & Decomissioning of aiconditioning split systems
LIC NO: KTR 407516
Nice to have
• Beacon Electrical & Refrigeration

```html
<!DOCTYPE html>
<html lang="en">
<head>
<meta charset="utf-8">
<title>Beacon Electrical &amp; Refrigeration – Business Card</title>
<link rel="stylesheet" href="https://fonts.googleapis.com/css2?family=Arimo:wght@400;700&family=Tinos&display=swap">
<style>
  :root {
    --backdrop: #d9d9d9;
    --card: #000000;
    --gold: #c9a21b;
    --white: #ffffff;
    --muted: #bdbdbd;
    --label: #111111;
  }
  * { margin: 0; padding: 0; box-sizing: border-box; }
  html, body {
    width: 1200px; height: 900px; overflow: hidden;
    background: var(--backdrop);
    font-family: "Arimo", Arial, sans-serif;
  }
  .stage { position: relative; width: 1200px; height: 900px; }
  .side-label {
    position: absolute;
    font-family: "Tinos", "Times New Roman", serif;
    font-size: 26px; color: var(--label); letter-spacing: 0.5px;
  }
  .side-label--front { left: 933px; top: 104px; }
  .side-label--back { left: 187px; top: 757px; }

  .card {
    position: absolute; width: 499px; height: 284px;
    background: var(--card);
    box-shadow: 2px 3px 6px rgba(0,0,0,0.35);
    color: var(--gold);
  }
  .card--front { left: 521px; top: 146px; }
  .card--back { left: 175px; top: 462px; }

  .brand { position: absolute; color: var(--gold); font-weight: 400; }
  .brand__name { display: block; line-height: 1; }
  .brand__trade { display: block; line-height: 1; }

  .card--front .brand { left: 54px; top: 104px; text-align: right; }
  .card--front .brand__name { font-size: 58px; letter-spacing: -0.5px; }
  .card--front .brand__trade { font-size: 14px; margin-top: 6px; }

  .divider {
    position: absolute; left: 319px; top: 106px;
    width: 1.5px; height: 72px; background: var(--gold);
  }
  .service {
    position: absolute; left: 334px; top: 108px;
    font-size: 13px; line-height: 17px; color: var(--gold);
  }

  .card--back .brand { left: 45px; top: 42px; text-align: right; }
  .card--back .brand__name { font-size: 42px; letter-spacing: -0.3px; }
  .card--back .brand__trade { font-size: 11px; margin-top: 4px; }

  .licence { position: absolute; left: 36px; top: 208px; display: flex; gap: 6px; align-items: flex-start; }
  .licence__badge { width: 33px; height: 33px; background: var(--gold); }
  .licence__text { font-size: 8.5px; line-height: 10px; color: var(--muted); margin-top: 8px; }

  .contact { position: absolute; left: 280px; top: 188px; color: var(--white); }
  .contact__name { font-size: 15px; font-weight: 700; margin-bottom: 7px; }
  .contact__line { display: flex; align-items: center; gap: 6px; font-size: 13px; line-height: 17px; }
  .contact__line svg { width: 11px; height: 11px; flex: none; }
</style>
</head>
<body>
<div class="stage">
  <div class="side-label side-label--front">FRONT</div>

  <section class="card card--front">
    <div class="brand">
      <span class="brand__name">Beacon</span>
      <span class="brand__trade">Electrical &amp; Refrigeration</span>
    </div>
    <div class="divider"></div>
    <p class="service">Installation and<br>Decomissioning of<br>Air Conditioning<br>Split Systems</p>
  </section>

  <section class="card card--back">
    <div class="brand">
      <span class="brand__name">Beacon</span>
      <span class="brand__trade">Electrical &amp; Refrigeration</span>
    </div>

    <div class="licence">
      <div class="licence__badge" role="img" aria-label="Authorised licence badge"></div>
      <p class="licence__text">LIC NO:<br>KTR 407516</p>
    </div>

    <div class="contact">
      <p class="contact__name">Peter Wollaston</p>
      <p class="contact__line">
        <svg viewBox="0 0 11 11" aria-hidden="true"><rect x="2.5" y="0.5" width="6" height="10" rx="1" fill="none" stroke="#c9a21b" stroke-width="1.2"/><rect x="3.8" y="2" width="3.4" height="4" fill="#c9a21b"/></svg>
        0457 819 302
      </p>
      <p class="contact__line">
        <svg viewBox="0 0 11 11" aria-hidden="true"><rect x="0.6" y="2.5" width="9.8" height="6.5" fill="none" stroke="#c9a21b" stroke-width="1.1"/><path d="M0.8 2.8 L5.5 6.3 L10.2 2.8" fill="none" stroke="#c9a21b" stroke-width="1.1"/></svg>
        prwollaston@tarvel.com.au
      </p>
    </div>
  </section>

  <div class="side-label side-label--back">BACK</div>
</div>
</body>
</html>
```